mint harbor is a crane lease company that leases generators, personell, riggers and dogman

I would like to revamp our design on the safety van that we use to go out on site , the picture we have on there at the moment needs to be more eye catching and focus on Saftey as its our safety van it needs to be noticed .The colours need to be red and white as our logo design and and most equipment is red or white .There also needs to be a picture of a tower crane as that is our buissness with the letter R for mintharbor to appear somewhere on the crane , please view our website www.mintharbor.com to get an idea of the colours snd what we are about.

Requirements
Must have
• Must be designed for the VAN , we already have our logo we want to put it on our safety van so it can be read by potential clients the picture on the van must have our logo on it with a focus on the crane and safety .I have uploaded a picture of one of our vans and our logo we will use our already exisiting logo , I would like a picture so we can put his on our safety van .
Nice to have
• please emphasise on red and white in the picture , and on a crane can we put the letter R to pop out !!

```html
<!DOCTYPE html>
<html lang="en">
<head>
<meta charset="utf-8">
<title>Mint Harbor Safety Van Wrap</title>
<link href="https://fonts.googleapis.com/css2?family=Jost:wght@500;600&family=Oswald:wght@600;700&family=Open+Sans:wght@700&display=swap" rel="stylesheet">
<style>
  :root {
    --brand-red: #d3202f;
    --deep-red: #a8141f;
    --charcoal: #2b2b2d;
    --jet: #1c1c1e;
    --panel-white: #f4f4f4;
    --silver: #d9dadc;
    --sky-top: #6f8fc7;
    --sky-low: #dfe7f2;
    --backdrop: #e6e6e6;
  }
  html, body { margin: 0; padding: 0; overflow: hidden; }
  body { width: 1200px; height: 1194px; background: var(--backdrop); }
  .wrap-sheet { display: block; width: 1200px; height: 1194px; }
  .brand-name { font-family: "Jost", sans-serif; font-weight: 600; letter-spacing: 1px; }
  .brand-tag { font-family: "Jost", sans-serif; font-weight: 500; letter-spacing: 1.5px; }
  .slogan { font-family: "Oswald", sans-serif; font-weight: 700; }
  .phone { font-family: "Oswald", sans-serif; font-weight: 700; }
  .web { font-family: "Open Sans", sans-serif; font-weight: 700; }
  .strapline { font-family: "Jost", sans-serif; font-weight: 500; letter-spacing: 4px; }
  .arrival { font-family: "Open Sans", sans-serif; font-weight: 700; letter-spacing: .5px; }
</style>
</head>
<body>
<svg class="wrap-sheet" viewBox="0 0 1200 1194" xmlns="http://www.w3.org/2000/svg">
  <defs>
    <linearGradient id="sky" x1="0" y1="0" x2="0" y2="1">
      <stop offset="0" stop-color="var(--sky-top)"/>
      <stop offset="1" stop-color="var(--sky-low)"/>
    </linearGradient>
    <linearGradient id="hoodShine" x1="0" y1="0" x2="0" y2="1">
      <stop offset="0" stop-color="#f2f2f2"/>
      <stop offset="1" stop-color="var(--silver)"/>
    </linearGradient>
    <clipPath id="sideBody">
      <path d="M480 125 L1080 120 Q1125 125 1132 165 L1140 440 Q1138 470 1110 470 L95 470 Q72 465 72 420 L80 345 Q95 315 200 280 L335 170 Q380 130 480 125 Z"/>
    </clipPath>
  </defs>

  <!-- ===== Side elevation ===== -->
  <g class="side-view">
    <g clip-path="url(#sideBody)">
      <rect class="body-base" x="60" y="110" width="1100" height="370" fill="var(--jet)"/>
      <rect class="sky-field" x="470" y="115" width="680" height="190" fill="url(#sky)"/>
      <rect class="crane-photo" role="img" aria-label="Tower crane photograph against a blue sky with a red letter on the jib" x="880" y="115" width="250" height="175" fill="#9fb3d4" opacity=".55"/>
      <polygon class="front-white" points="60,330 200,300 440,295 330,480 60,480" fill="var(--panel-white)"/>
      <polygon class="red-band" points="452,292 1140,288 1140,470 350,470" fill="var(--brand-red)"/>
      <polygon class="red-edge" points="440,296 452,292 350,470 336,470" fill="var(--deep-red)"/>
      <path class="band-accent" d="M935 370 L975 342 L1140 340 L1140 350 L980 352 L945 376 Z" fill="#fff" opacity=".85"/>
      <rect class="roof-stripe" x="450" y="280" width="690" height="6" fill="#fff" opacity=".8"/>
      <polygon class="lower-strip" points="372,432 1140,428 1140,470 350,470" fill="var(--charcoal)"/>
      <path class="cab-window" d="M345 170 Q380 140 505 140 L505 270 L300 272 Z" fill="#3b3e43"/>
    </g>
    <circle class="wheel" cx="212" cy="470" r="58" fill="var(--jet)"/>
    <circle class="rim" cx="212" cy="470" r="36" fill="#b9bcc0"/>
    <circle class="wheel" cx="920" cy="470" r="58" fill="var(--jet)"/>
    <circle class="rim" cx="920" cy="470" r="36" fill="#b9bcc0"/>

    <g class="logo-pill">
      <rect x="512" y="152" width="360" height="72" rx="36" fill="var(--charcoal)"/>
      <circle cx="548" cy="188" r="12" fill="var(--brand-red)"/>
      <text class="brand-name" x="574" y="192" font-size="34" fill="#fff">MINT HARBOR</text>
      <text class="brand-tag" x="576" y="213" font-size="15" fill="#fff">CRANES AND PERSONNEL</text>
    </g>
    <text class="slogan" x="522" y="284" font-size="56" textLength="374" lengthAdjust="spacingAndGlyphs" fill="var(--charcoal)">WE R SAFETY FIRST</text>

    <g class="phone-icon" transform="translate(470 358)">
      <circle r="26" fill="#fff"/>
      <path d="M-10 -12 q-6 10 3 22 q10 10 20 4 l-5 -7 q-5 3 -10 -3 q-6 -6 -2 -10 z" fill="var(--brand-red)"/>
    </g>
    <text class="phone" x="508" y="382" font-size="72" textLength="380" lengthAdjust="spacingAndGlyphs" fill="#fff">1300 555 210</text>
    <g class="web-icon" transform="translate(458 412)" fill="none" stroke="#fff" stroke-width="2">
      <circle r="11"/><ellipse rx="5" ry="11"/><line x1="-11" y1="0" x2="11" y2="0"/>
    </g>
    <text class="web" x="480" y="420" font-size="27" fill="#fff">www.mintharbor.com</text>
    <text class="strapline" x="372" y="458" font-size="15" fill="#fff">THE FIRST CHOICE IN MATERIAL HANDLING</text>
    <text class="arrival" x="907" y="330" font-size="13.5" fill="#fff">SAFETY VAN HAS ARRIVED</text>
    <text class="brand-name door-mark" x="296" y="376" font-size="20" text-anchor="middle" fill="var(--brand-red)">MINT HARBOR</text>
  </g>

  <!-- ===== Front elevation ===== -->
  <g class="front-view">
    <path class="windscreen" d="M150 680 Q160 664 200 664 L490 664 Q530 664 540 680 L570 800 L120 800 Z" fill="#2a2c30"/>
    <rect class="mirror" x="70" y="766" width="50" height="34" rx="8" fill="var(--jet)"/>
    <rect class="mirror" x="570" y="766" width="50" height="34" rx="8" fill="var(--jet)"/>
    <path class="hood" d="M118 796 L572 796 Q578 830 572 868 L118 868 Q112 830 118 796 Z" fill="url(#hoodShine)"/>
    <text class="brand-name" x="280" y="842" font-size="27" fill="var(--brand-red)">MINT HARBOR</text>
    <text class="brand-tag" x="282" y="857" font-size="12.5" fill="var(--brand-red)">CRANES AND PERSONNEL</text>
    <circle cx="258" cy="832" r="10" fill="var(--brand-red)"/>
    <rect class="grille-band" x="108" y="866" width="474" height="48" fill="#e1e1e1"/>
    <rect x="200" y="874" width="290" height="32" fill="var(--jet)"/>
    <circle cx="133" cy="890" r="18" fill="#f4f4f4" stroke="#888"/>
    <circle cx="557" cy="890" r="18" fill="#f4f4f4" stroke="#888"/>
    <path class="bumper" d="M104 912 L586 912 L578 1062 L112 1062 Z" fill="var(--jet)"/>
    <rect x="196" y="952" width="280" height="38" fill="#111"/>
    <rect x="110" y="1060" width="60" height="62" rx="8" fill="#111"/>
    <rect x="520" y="1060" width="60" height="62" rx="8" fill="#111"/>
  </g>

  <!-- ===== Rear elevation ===== -->
  <g class="rear-view">
    <path class="rear-body" d="M690 664 L1090 664 Q1108 668 1110 700 L1112 1064 L660 1064 L662 700 Q664 668 690 664 Z" fill="var(--panel-white)"/>
    <path class="roof-red" d="M690 664 L1090 664 Q1108 668 1110 700 L662 700 Q664 668 690 664 Z" fill="var(--brand-red)"/>
    <rect class="rear-window" x="702" y="684" width="364" height="140" rx="16" fill="var(--charcoal)"/>
    <g class="cert-badges">
      <rect x="774" y="692" width="72" height="26" rx="13" fill="#fff" stroke="#2f9d45" stroke-width="3"/>
      <rect x="850" y="692" width="72" height="26" rx="13" fill="#fff" stroke="var(--brand-red)" stroke-width="3"/>
      <rect x="926" y="692" width="72" height="26" rx="13" fill="#fff" stroke="#f0a526" stroke-width="3"/>
    </g>
    <circle cx="770" cy="768" r="12" fill="#fff"/>
    <text class="brand-name" x="792" y="778" font-size="30" fill="#fff">MINT HARBOR</text>
    <text class="brand-tag" x="794" y="798" font-size="14" fill="#fff">CRANES AND PERSONNEL</text>
    <rect x="662" y="864" width="38" height="70" fill="var(--deep-red)"/>
    <rect x="1070" y="864" width="38" height="70" fill="var(--deep-red)"/>
    <g class="phone-icon" transform="translate(738 855)">
      <circle r="20" fill="var(--brand-red)"/>
      <path d="M-8 -9 q-5 8 2 17 q8 8 16 3 l-4 -6 q-4 2 -8 -2 q-5 -5 -2 -8 z" fill="#fff"/>
    </g>
    <text class="phone" x="768" y="878" font-size="52" textLength="276" lengthAdjust="spacingAndGlyphs" fill="var(--brand-red)">1300 555 210</text>
    <rect class="plate-recess" x="828" y="896" width="148" height="26" fill="var(--charcoal)"/>
    <rect class="lower-band" x="662" y="944" width="448" height="64" fill="var(--charcoal)"/>
    <g class="web-icon" transform="translate(737 972)" fill="none" stroke="#fff" stroke-width="2">
      <circle r="11"/><ellipse rx="5" ry="11"/><line x1="-11" y1="0" x2="11" y2="0"/>
    </g>
    <text class="web" x="758" y="981" font-size="26" fill="#fff">www.mintharbor.com</text>
    <rect class="rear-bumper" x="660" y="1008" width="452" height="56" fill="var(--jet)"/>
    <rect x="664" y="1060" width="56" height="62" rx="8" fill="#111"/>
    <rect x="1052" y="1060" width="56" height="62" rx="8" fill="#111"/>
  </g>
</svg>
</body>
</html>
```